Hourgala promotional materials

Hourgala is a Canada-wide event that matches non-profits to skilled volunteers. The first part of the evening, attendees mix and mingle with the non-profits in the room. The second half of the evening is a a silent art auction where attendees bid their time, not their money, on artwork that we have purchased from local emerging artists. A successful bid maxes out at 100 volunteer hours. The Art-Winner has twelve months to complete their pledge before taking their artwork home as a sign of their good will.

We are not looking for someone to design a promotional postcards that sums up and reflects what we do.

We would like to play off of our current logo and colour palate- does not have to be directly lifted, it can be an interpretive riff. We want our branding to be instantly recognizable.

Here is a link to a video about what we do: http://www.hourgala-events.ca/

Target Market(s)

Young professionals who are community minded and interested in cultural products. We skew female and 25-40.

Industry/Entity Type

Artists

Font styles to use
Sans Serif

Requirements
Must have
• a) Hourgala colours: Green #7ac044, Grey #3e3e40
b) Hourgala logo should always use the 3 colour EPS version

Link to the Hourgala Logo:
https://hourgala.filedrop-host.com/hourgalalogo
Nice to have
• We want it to be modern, clean, fun, easy to read. The Hourgala can be complex to explain, so simplicity is key. We are open to "riffs" on our logo. For example, if you want to take one aspect or theme expressed by our logo and incorporate it into the design, we'd be interested to see what you could come up with. Nothing too trendy and faddish please as we'd like to use these designs across several seasons.
Should not have
• We don't want overly engineered or complex designs that we can't adapt.

```html
<!DOCTYPE html>
<html lang="en">
<head>
<meta charset="utf-8">
<title>Hourgala – Quote Card</title>
<link rel="stylesheet" href="https://fonts.googleapis.com/css2?family=Montserrat:wght@600;700;800&display=swap">
<style>
  :root {
    --card-green: #aaf79d;
    --paper-white: #ffffff;
    --ink-black: #111111;
  }
  html, body {
    margin: 0;
    padding: 0;
    width: 847px;
    height: 1200px;
    overflow: hidden;
    background: var(--card-green);
  }
  .quote-card {
    position: relative;
    width: 847px;
    height: 1200px;
    background: var(--card-green);
    font-family: "Montserrat", Arial, sans-serif;
    color: var(--paper-white);
  }
  .rule {
    position: absolute;
    left: 276px;
    width: 293px;
    background: var(--paper-white);
  }
  .rule--top { top: 157px; height: 10px; }
  .rule--middle { top: 795px; height: 9px; }
  .rule--bottom { top: 887px; height: 6px; }
  .quote-text {
    position: absolute;
    top: 218px;
    left: 0;
    width: 847px;
    margin: 0;
    text-align: center;
    font-weight: 800;
    font-size: 53px;
    line-height: 75.5px;
    letter-spacing: 0.2px;
  }
  .quote-author {
    position: absolute;
    top: 836px;
    left: 0;
    width: 847px;
    margin: 0;
    text-align: center;
    font-weight: 700;
    font-size: 22px;
    line-height: 34px;
  }
  .brand-tab {
    position: absolute;
    left: 276px;
    top: 994px;
    width: 293px;
    height: 206px;
  }
  .brand-tab svg {
    position: absolute;
    inset: 0;
    display: block;
  }
  .brand-name {
    position: absolute;
    top: 98px;
    left: 0;
    width: 293px;
    margin: 0;
    text-align: center;
    font-weight: 600;
    font-size: 28px;
    line-height: 36px;
    color: var(--ink-black);
  }
  .brand-url {
    position: absolute;
    top: 152px;
    left: 0;
    width: 293px;
    margin: 0;
    text-align: center;
    font-weight: 800;
    font-size: 18px;
    color: var(--ink-black);
  }
</style>
</head>
<body>
  <main class="quote-card">
    <div class="rule rule--top"></div>
    <p class="quote-text">Yesterday’s the<br>past, tomorrow’s<br>the future, but today<br>is a gift. That’s why<br>it’s called the<br>present.</p>
    <div class="rule rule--middle"></div>
    <p class="quote-author">Dana Whitlock</p>
    <div class="rule rule--bottom"></div>

    <footer class="brand-tab">
      <svg width="293" height="206" viewBox="0 0 293 206" aria-hidden="true">
        <polygon points="0,0 146.5,28 293,0 293,206 0,206" fill="var(--paper-white)"/>
      </svg>
      <p class="brand-name">Hourgala</p>
      <p class="brand-url">www.hourgala-events.ca</p>
    </footer>
  </main>
</body>
</html>
```